Energy drink company looking for a complete can design

Design an energy drink can label using an established trademarked logo along with mandatory nutrition and ingredients table.
We would like to see 3 versions or samples to judge:
1. can design over a black background - called dark color version
2. can design over a white background - called light color version
3. can design over a grey/silver background - called balanced color version

Target Market(s)

USA

Requirements
Must have
• the phrase "yes kelvora energy drink" "yes kelvora" and "ALL Natural Libido Enhancing energy drink" must be on the can somewhere

```html
<!DOCTYPE html>
<html lang="en">
<head>
<meta charset="utf-8">
<title>Yes Kelvora Energy Drink – Can Label</title>
<link href="https://fonts.googleapis.com/css2?family=Montserrat:wght@400;500&family=Graduate&family=Roboto+Condensed:wght@300;400;700&family=Arimo:wght@400;700;900&display=swap" rel="stylesheet">
<style>
  :root {
    --page: #ffffff;
    --rule: #9a9a9a;
    --ink: #1a1a1a;
    --band: #d63a2f;
    --gold: #f2c744;
    --gold-deep: #d9a521;
    --lip: #c8242b;
    --lip-light: #e0565a;
  }
  * { margin: 0; padding: 0; box-sizing: border-box; }
  html, body { width: 1198px; height: 1200px; overflow: hidden; background: var(--page); }
  .canvas { position: relative; width: 1198px; height: 1200px; }

  .dieline {
    position: absolute; left: 166px; top: 279px; width: 909px; height: 647px;
    border: 2px solid var(--rule); background: var(--page);
  }
  .panel-divider { position: absolute; top: 0; bottom: 0; width: 2px; background: var(--rule); }
  .panel-divider.left { left: 246px; }
  .panel-divider.right { left: 667px; }

  .front-title {
    position: absolute; left: 248px; width: 419px; text-align: center;
    font-family: "Montserrat", sans-serif; color: var(--ink); letter-spacing: 0.12em;
  }
  .front-title.kicker { top: 38px; font-size: 15px; font-weight: 500; }
  .front-title.main { top: 62px; font-size: 24px; font-weight: 400; letter-spacing: 0.14em; }

  .hero-art { position: absolute; left: 358px; top: 177px; width: 200px; height: 132px; }

  .brand-name {
    position: absolute; left: 248px; width: 419px; top: 318px; text-align: center;
    font-family: "Roboto Condensed", sans-serif; font-weight: 300;
    font-size: 84px; line-height: 1; color: var(--gold-deep);
  }

  .claim-band {
    position: absolute; left: 248px; top: 490px; width: 419px; height: 155px;
    background: var(--band); text-align: center; padding-top: 44px;
  }
  .claim-band .claim-head {
    font-family: "Graduate", serif; font-size: 25px; color: var(--gold); letter-spacing: 0.04em;
  }
  .claim-band .claim-sub {
    font-family: "Roboto Condensed", sans-serif; font-weight: 400; font-size: 23px;
    color: var(--gold); margin-top: 2px;
  }

  .nutrition {
    position: absolute; left: 49px; top: 170px; width: 106px;
    border: 1px solid var(--ink); padding: 2px 3px;
    font-family: "Arimo", sans-serif; color: var(--ink); font-size: 4.6px; line-height: 1.35;
  }
  .nutrition h3 { font-size: 10px; font-weight: 900; line-height: 1.1; border-bottom: 1px solid var(--ink); }
  .nutrition .serving { font-weight: 700; font-size: 5px; border-bottom: 4px solid var(--ink); padding: 1px 0; }
  .nutrition .calories { display: flex; justify-content: space-between; font-weight: 900; font-size: 9px; border-bottom: 2px solid var(--ink); }
  .nutrition .row { display: flex; justify-content: space-between; border-bottom: 0.5px solid var(--ink); }
  .nutrition .row.indent { padding-left: 5px; }
  .nutrition .row.bold { font-weight: 700; }
  .nutrition .row.heavy { border-bottom: 4px solid var(--ink); }
  .nutrition .dv { text-align: right; font-weight: 700; border-bottom: 0.5px solid var(--ink); }
  .nutrition .footnote { font-size: 3.4px; line-height: 1.3; padding-top: 1px; }

  .label-text {
    position: absolute; font-family: "Arimo", sans-serif; color: var(--ink); font-size: 5.6px; line-height: 1.75;
  }
  .label-text.allergens { left: 14px; top: 404px; }
  .label-text.ingredients { left: 14px; top: 413px; width: 210px; display: flex; gap: 3px; }
  .label-text .term { font-weight: 700; flex: none; }
</style>
</head>
<body>
<div class="canvas">
  <div class="dieline">
    <div class="panel-divider left"></div>
    <div class="panel-divider right"></div>

    <section class="nutrition" aria-label="Nutrition Facts">
      <h3>Nutrition Facts</h3>
      <div class="serving">Serving size &nbsp; 12 fl oz (355 mL)</div>
      <div>Amount per serving</div>
      <div class="calories"><span>Calories</span><span>90</span></div>
      <div class="dv">% Daily Value*</div>
      <div class="row bold"><span>Total Fat 0g</span><span>0%</span></div>
      <div class="row indent"><span>Saturated Fat 0g</span><span>0%</span></div>
      <div class="row indent"><span>Trans Fat 0g</span><span></span></div>
      <div class="row bold"><span>Cholesterol 0mg</span><span>0%</span></div>
      <div class="row bold"><span>Sodium 0mg</span><span>0%</span></div>
      <div class="row bold"><span>Total Carbohydrate 21g</span><span>8%</span></div>
      <div class="row indent"><span>Dietary Fiber 0g</span><span>0%</span></div>
      <div class="row indent"><span>Total Sugars 16g</span><span></span></div>
      <div class="row indent"><span>Includes 0g Added Sugars</span><span>0%</span></div>
      <div class="row bold heavy"><span>Protein 0g</span><span></span></div>
      <div class="row"><span>Vitamin D 0mcg</span><span>0%</span></div>
      <div class="row"><span>Calcium 10mg</span><span>0%</span></div>
      <div class="row"><span>Iron 0mg</span><span>0%</span></div>
      <div class="row"><span>Potassium 200mg</span><span>4%</span></div>
      <div class="row"><span>Vitamin C 90mg</span><span>100%</span></div>
      <div class="row"><span>Niacin 16mg</span><span>100%</span></div>
      <div class="row"><span>Vitamin B6 1.7mg</span><span>100%</span></div>
      <div class="row"><span>Vitamin B12 2.4mcg</span><span>100%</span></div>
      <div class="row"><span>Pantothenic Acid 5mg</span><span>100%</span></div>
      <div class="row heavy"><span>Zinc 2mg</span><span>20%</span></div>
      <p class="footnote">*The % Daily Value tells you how much a nutrient in a serving contributes to a daily diet. 2,000 calories a day is used for general nutrition advice.</p>
    </section>

    <p class="label-text allergens"><span class="term">Allergens:</span> None</p>
    <p class="label-text ingredients"><span class="term">Ingredients:</span><span>Filtered Water, Organic Peach Juice Concentrate, Organic White Grape Juice Concentrate, Organic Pear Juice Concentrate, Organic Pineapple Juice Concentrate, Organic Natural Flavors, Horny Goat Weed Extract, Citric Acid, L-Arginine, Taurine, Maca Root Extract, Ascorbic Acid, Natural Caffeine from Green Tea, Panax Ginseng, Organic Monk Fruit, Ginkgo Biloba, Stevia Reb M, Niacinamide, Zinc Citrate, Calcium Pantothenate, Pyridoxine Hydrochloride, Cyanocobalamin</span></p>

    <p class="front-title kicker">YES KELVORA</p>
    <p class="front-title main">ENERGY DRINK</p>

    <svg class="hero-art" viewBox="0 0 200 132" role="img" aria-label="Illustration of red lips biting a pineapple slice dripping with golden juice">
      <defs>
        <radialGradient id="lipTone" cx="50%" cy="45%" r="60%">
          <stop offset="0%" stop-color="var(--lip-light)"/>
          <stop offset="100%" stop-color="var(--lip)"/>
        </radialGradient>
      </defs>
      <ellipse cx="100" cy="58" rx="98" ry="52" fill="url(#lipTone)"/>
    </svg>

    <p class="brand-name">yes kelvora</p>

    <div class="claim-band">
      <p class="claim-head">ALL NATURAL LIBIDO</p>
      <p class="claim-sub">Enhancing energy drink</p>
    </div>
  </div>
</div>
</body>
</html>
```